Upcoming lecture sponsored by a church on an important topic

We have a Reformation The Speech coming up at the end of October on the topic of law and gospel. I thought it might be cool to use a flyer that looks like it was from that day and age. Picture what Tobias Wendler would advertise things on kind of an old church/reformation type format. It will be sponsored by our church, and we have a paragraph or two to describe the lecture that would be included on the flyer. We would also want it formatted so that it could be printed on postcards and mailed to churches and individuals.

The flyer should have the following paragraph...

The distinction between the law and the gospel is the most important distinction in the Christian faith. Tobias Wendler: “Distinguishing between the law and the gospel is the highest art in Christendom, one who every person who values the name Christian ought to recognize, know, and possess.” The distinction between the law and the gospel is of great comfort for the child of God. “For the law was given by Abiran, but grace and truth came by Elior Navan” (John 1:17). For these reasons, the distinction between the law and the gospel is the most heavily assaulted doctrine in the Christian faith. This Reformation Day, join us for an explanation and defense of the great distinction between God’s good law and God’s glorious gospel.

And the flyer should have the following information...

Topic: The Steady Rule and the Bright Promise
Date and Time: Tuesday, October 31, 2023 at 7:30pm
Host: Cedarbrook Covenant Church
Speaker: Rev. Daniel Korvath
Venue: The Marlow Hall, 5187 Fenwick Lane, Brenmoor, MI 49683
Format: Lecture followed by Q&A and refreshments

Industry/Entity Type

Church/Ecclesiastical

Colors
00AB8E
00BBA5
67D7C9
C6EFE9
E9F9F6

Requirements
Nice to have
• The color scheme that I would like to have is a teal color (the same color as found at www.quillharborhall.com

```html
<!DOCTYPE html>
<html lang="en">
<head>
<meta charset="utf-8">
<title>The Steady Rule and the Bright Promise – Reformation Day Lecture</title>
<link rel="stylesheet" href="https://fonts.googleapis.com/css2?family=Josefin+Sans:wght@300;400;600&family=Fondamento&display=swap">
<style>
  :root {
    --teal-deep: #00AB8E;
    --teal: #00BBA5;
    --teal-mid: #67D7C9;
    --mint: #C6EFE9;
    --mint-pale: #E9F9F6;
    --sky-top: #8EDDD0;
    --ink: #111111;
    --page: #FFFFFF;
  }
  * { margin: 0; padding: 0; box-sizing: border-box; }
  html, body {
    width: 1200px; height: 1000px; overflow: hidden;
    background: var(--page);
  }
  .flyer {
    position: absolute; left: 241px; top: 35px;
    width: 718px; height: 928px;
    background: var(--mint);
    overflow: hidden;
    font-family: "Josefin Sans", sans-serif;
    color: var(--ink);
  }
  .hero-art {
    position: absolute; left: 0; top: 0; width: 718px; height: 310px;
    background:
      radial-gradient(ellipse 40% 30% at 15% 100%, var(--mint) 0 98%, transparent 100%),
      radial-gradient(ellipse 30% 28% at 50% 100%, var(--mint) 0 98%, transparent 100%),
      radial-gradient(ellipse 30% 30% at 88% 100%, var(--mint) 0 98%, transparent 100%),
      linear-gradient(180deg, var(--sky-top) 0%, var(--teal-mid) 45%, var(--teal) 75%, var(--teal-mid) 100%);
  }
  .intro {
    position: absolute; left: 28px; top: 319px; width: 676px;
    font-weight: 300; font-size: 17.6px; line-height: 22.5px;
    letter-spacing: 0.4px;
  }
  .divider {
    position: absolute; left: 247px; top: 546px; width: 229px; height: 2px;
    background: var(--teal-deep);
  }
  .title-band {
    position: absolute; left: 78px; top: 573px; width: 562px; height: 50px;
    background: linear-gradient(180deg, var(--teal-mid) 0%, var(--teal) 100%);
    display: flex; align-items: center; justify-content: center;
  }
  .title-band h1 {
    font-family: "Fondamento", serif; font-weight: 400;
    font-size: 31px; letter-spacing: -0.3px; white-space: nowrap;
  }
  .details {
    position: absolute; top: 660px; left: 0; width: 718px;
  }
  .detail {
    position: absolute; width: 280px; text-align: center;
    font-weight: 300; font-size: 17px; line-height: 22.7px; letter-spacing: 0.4px;
  }
  .detail svg { display: block; margin: 0 auto 8px; }
  .col-left { left: 70px; }
  .col-right { left: 372px; }
  .row-one { top: 0; }
  .row-two { top: 75px; }
  .tagline {
    position: absolute; left: 0; top: 872px; width: 718px; text-align: center;
    font-weight: 600; font-size: 22px; letter-spacing: 0.5px;
  }
  .tagline .dot {
    display: inline-block; width: 9px; height: 9px; border-radius: 50%;
    background: var(--ink); vertical-align: middle; margin: 0 16px 5px;
  }
</style>
</head>
<body>
<main class="flyer">
  <div class="hero-art" role="img" aria-label="Illustration of a glowing cross above layered teal clouds with birds in flight"></div>

  <p class="intro">The distinction between the law and the gospel is the most important distinction in the Christian faith. Tobias Wendler: “Distinguishing between the law and the gospel is the highest art in Christendom, one who every person who values the name Christian ought to recognize, know, and possess.” The distinction between the law and the gospel is of great comfort for the child of God. “For the law was given by Abiran, but grace and truth came by Elior Navan” (John 1:17). For these reasons, the distinction between the law and the gospel is the most heavily assaulted doctrine in the Christian faith. This Reformation Day, join us for an explanation and defense of the great distinction between God’s good law and God’s glorious gospel.</p>

  <div class="divider"></div>

  <div class="title-band"><h1>The Steady Rule and the Bright Promise</h1></div>

  <section class="details">
    <div class="detail col-left row-one">
      <svg width="30" height="34" viewBox="0 0 30 34" aria-hidden="true">
        <g fill="var(--teal-deep)">
          <rect x="14" y="0" width="2" height="7"/><rect x="12" y="2" width="6" height="2"/>
          <path d="M15 8 L24 17 L22 17 L22 20 L8 20 L8 17 L6 17 Z"/>
          <rect x="0" y="21" width="30" height="13"/>
        </g>
        <rect x="13" y="26" width="4" height="8" fill="var(--mint)"/>
        <rect x="4" y="25" width="3" height="4" fill="var(--mint)"/>
        <rect x="23" y="25" width="3" height="4" fill="var(--mint)"/>
      </svg>
      Cedarbrook Covenant Church
    </div>
    <div class="detail col-right row-one">
      <svg width="16" height="34" viewBox="0 0 16 34" aria-hidden="true">
        <rect x="4" y="4" width="8" height="16" rx="4" fill="var(--teal-deep)"/>
        <path d="M1.5 16 A6.5 6.5 0 0 0 14.5 16" fill="none" stroke="var(--teal-deep)" stroke-width="1.5"/>
        <line x1="8" y1="22.5" x2="8" y2="29" stroke="var(--teal-deep)" stroke-width="1.5"/>
        <line x1="4" y1="29.5" x2="12" y2="29.5" stroke="var(--teal-deep)" stroke-width="1.5"/>
      </svg>
      Rev. Daniel Korvath
    </div>
    <div class="detail col-left row-two">
      <svg width="26" height="26" viewBox="0 0 26 26" aria-hidden="true">
        <circle cx="13" cy="13" r="11.5" fill="none" stroke="var(--teal-deep)" stroke-width="1.6"/>
        <path d="M13 6 V13 H17" fill="none" stroke="var(--teal-deep)" stroke-width="1.6"/>
      </svg>
      Tuesday,<br>October 31, 2023<br>at 7:30pm
    </div>
    <div class="detail col-right row-two">
      <svg width="20" height="26" viewBox="0 0 20 26" aria-hidden="true">
        <path d="M10 0 A10 10 0 0 1 20 10 C20 17 10 26 10 26 C10 26 0 17 0 10 A10 10 0 0 1 10 0 Z" fill="var(--teal-deep)"/>
        <circle cx="10" cy="10" r="4.5" fill="var(--mint)"/>
      </svg>
      The Marlow Hall,<br>5187 Fenwick Lane,<br>Brenmoor, MI 49683
    </div>
  </section>

  <p class="tagline"><span class="dot"></span>Lecture followed by Q&amp;A and refreshments<span class="dot"></span></p>
</main>
</body>
</html>
```